stationary for hygienic company

We need a stationary design for hygienic company which provides public high end sanitary products and high end public lavatory.
We need a fresh and clean style stationary
we want the following things:
* logo (redesigned in eps/vector)
* Letterhead (with company details)
* letterhead (without company details)
* Business card
* note block
* ballpoint
* etcetera (a complete package)

```html
<!DOCTYPE html>
<html lang="en">
<head>
<meta charset="utf-8">
<title>Velunra – Business Card</title>
<link href="https://fonts.googleapis.com/css2?family=Open+Sans:wght@300;400;700&display=swap" rel="stylesheet">
<style>
  :root {
    --backdrop: #ece9e4;
    --card-dark: #0b0b0b;
    --card-light: #f4f4f2;
    --ink-dark: #1a1a1a;
    --ink-light: #ffffff;
    --accent-cyan: #5bbfdc;
    --accent-magenta: #b62a9a;
    --rule: #2a2a2a;
  }
  * { margin: 0; padding: 0; box-sizing: border-box; }
  html, body {
    width: 1200px; height: 756px; overflow: hidden;
    background: var(--backdrop);
    font-family: "Open Sans", Arial, sans-serif;
  }
  .card-set {
    position: absolute; inset: 0;
    display: flex; align-items: center; justify-content: center; gap: 60px;
  }
  .card {
    width: 500px; height: 290px; border-radius: 28px;
    position: relative;
    box-shadow: 0 6px 18px rgba(0,0,0,0.18);
  }
  .card--front { background: var(--card-dark); color: var(--ink-light); }
  .card--back { background: var(--card-light); color: var(--ink-dark); }

  .brand { display: flex; flex-direction: column; align-items: flex-start; }
  .brand__mark {
    width: 56px; height: 56px; border-radius: 50%;
    background: linear-gradient(135deg, var(--accent-cyan), var(--accent-magenta));
    margin-bottom: 8px;
  }
  .brand__name { font-weight: 300; font-size: 58px; line-height: 1; letter-spacing: -1px; }
  .brand__tagline { font-weight: 300; font-size: 21px; margin-top: 2px; }

  .card--front .brand { position: absolute; left: 150px; top: 42px; }
  .card--front .brand__url { font-weight: 700; font-size: 13px; margin-top: 14px; align-self: flex-end; }

  .card--back .brand { position: absolute; left: 30px; bottom: 36px; }
  .card--back .brand__name { font-size: 50px; }
  .card--back .brand__tagline { font-size: 18px; }
  .brand__note { font-size: 6px; align-self: flex-end; margin-top: 1px; }

  .card__divider {
    position: absolute; left: 262px; top: 32px; bottom: 32px;
    width: 1px; background: var(--rule);
  }
  .contact { position: absolute; left: 282px; top: 38px; font-size: 12.5px; line-height: 1.45; }
  .contact__name { font-weight: 700; font-size: 13px; }
  .contact__role { margin-bottom: 8px; }
  .contact__lines { list-style: none; margin-top: 10px; }
  .contact__lines li { display: flex; align-items: center; gap: 7px; }
  .contact__lines svg { width: 11px; height: 11px; flex: none; }
</style>
</head>
<body>
  <main class="card-set">
    <section class="card card--front" aria-label="Business card front">
      <div class="brand">
        <span class="brand__mark"></span>
        <span class="brand__name">Velunra</span>
        <span class="brand__tagline">Boutique Hygienique</span>
        <span class="brand__url">www.velunra.ma</span>
      </div>
    </section>

    <section class="card card--back" aria-label="Business card back">
      <div class="brand">
        <span class="brand__mark"></span>
        <span class="brand__name">Velunra</span>
        <span class="brand__tagline">Boutique Hygienique</span>
        <span class="brand__note">marque déposée</span>
      </div>
      <span class="card__divider"></span>
      <div class="contact">
        <p class="contact__name">MARCUS HALE</p>
        <p class="contact__role">Owner</p>
        <p>40120 Marrakesh, Morocco</p>
        <p>2815 N. Alder Lane, Suite 300</p>
        <p>Fresno, CA 93711</p>
        <ul class="contact__lines">
          <li><svg viewBox="0 0 12 12"><rect x="3" y="0.5" width="6" height="11" rx="1" fill="none" stroke="currentColor"/></svg>+212 600-410100</li>
          <li><svg viewBox="0 0 12 12"><path d="M2 1l3 2-1 2c1 2 2 3 3 3l2-1 2 3-2 1C4 11 1 7 1 3z" fill="currentColor"/></svg>+212 600-410122</li>
          <li><svg viewBox="0 0 12 12"><rect x="1" y="4" width="10" height="7" fill="none" stroke="currentColor"/><rect x="3" y="1" width="6" height="3" fill="none" stroke="currentColor"/></svg>+212 600-410133</li>
          <li><svg viewBox="0 0 12 12"><rect x="0.5" y="2.5" width="11" height="7" fill="none" stroke="currentColor"/><path d="M1 3l5 4 5-4" fill="none" stroke="currentColor"/></svg>info@velunra.ma</li>
        </ul>
      </div>
    </section>
  </main>
</body>
</html>
```